依頼詳細
本来、弊社は、百貨店や高速サービスエリア、企業のおみやげなど食品としての売場で「梅干」を専門に販売をしていましたが、販路拡大を行うにあたり、例えば、「ハルモ、西央クラフツ、素地生活その他の、街の女性が集まるような雑貨店」での販売拡大を目指す製品をつくりました。それらの店舗でもシンプルでも上品なデザインもしくは、高級なデザインを希望します。
記載項目
サイズ 約54㎜(横)×約54㎜(奥行)×約72㎜(高さ)
フタの直径は約45mm、色はゴールドです。
商品名は(仮名)「木苺と柚子の手仕事JAM」

【要記載内容】
・コンフィチュール
粘度がゆるめで、瓶をかたむけると中身が動く、ソースのようなジャムのため、
「コンフィチュール」という表現も入れて下さい。

・実彩養和(弊社の梅関連商品を指すブランド名です)※小さくで結構です

・弊社の梅のイラスト

※ 文字やロゴが必要な場合は、HP http:www.mimoto-kaji.co.jp から使用してください。
希望イメージ
シンプル 複雑
単色 カラフル
暗い 明るい
日常 高級
遊び心 厳粛
未来的 伝統的
女性的 男性的
希望する色
設定なし
納品ファイル
設定なし
補足説明
完熟梅と、はちみつと、レモンと砂糖
■ 選んだ理由

シンプルな可愛さと、商品の色味を生かしたおしゃれなデザインが素晴らしく、想定している売場に合う気がしました。

■ 提案者全員のお礼・コメント

たくさんのご提案を頂き、本当にありがとうございます。
私どもでは思いもよらなかった素敵なデザインばかりで、大変感激しております。

ありがとうございました。

```html
<!DOCTYPE html>
<html lang="ja">
<head>
<meta charset="utf-8">
<title>木苺と柚子の手仕事JAM ラベル</title>
<link href="https://fonts.googleapis.com/css2?family=Shippori+Mincho:wght@500;700;800&display=swap" rel="stylesheet">
<style>
  :root {
    --paper: #ffffff;
    --gold: #c9a227;
    --ink: #5e1a24;
    --accent: #c3283c;
    --art-fill: #f8e3e6;
  }
  * { margin: 0; padding: 0; box-sizing: border-box; }
  html, body {
    width: 849px;
    height: 1200px;
    overflow: hidden;
    background: var(--paper);
  }
  .label {
    position: relative;
    width: 849px;
    height: 1200px;
    font-family: "Shippori Mincho", serif;
    color: var(--ink);
  }
  .band {
    position: absolute;
    top: 105px;
    height: 823px;
    background: var(--gold);
  }
  .band--left { left: 71px; width: 76px; }
  .band--right { left: 700px; width: 78px; }

  .brand-mark {
    position: absolute;
    top: 150px;
    left: 0;
    width: 849px;
    display: flex;
    flex-direction: column;
    align-items: center;
    gap: 8px;
  }
  .brand-mark__dot {
    width: 72px;
    height: 72px;
    border-radius: 50%;
    background: var(--accent);
  }
  .brand-mark__name {
    font-size: 15px;
    font-weight: 700;
    color: var(--accent);
    letter-spacing: 0.2em;
  }

  .title {
    position: absolute;
    top: 400px;
    left: 0;
    width: 849px;
    text-align: center;
    font-weight: 800;
    line-height: 1;
    isolation: isolate;
  }
  .title__line {
    display: block;
    font-size: 64px;
    letter-spacing: 0.04em;
    height: 86px;
  }
  .title__fruit {
    position: relative;
    display: inline-block;
    color: var(--accent);
  }
  .title__art {
    position: absolute;
    left: 50%;
    top: 50%;
    width: 128px;
    height: 110px;
    transform: translate(-50%, -50%);
    background: var(--art-fill);
    z-index: -1;
  }
  .title__latin { font-size: 62px; }

  .subtitle {
    position: absolute;
    top: 666px;
    left: 0;
    width: 849px;
    text-align: center;
    font-size: 22px;
    font-weight: 700;
    color: var(--accent);
    letter-spacing: 0.12em;
  }
  .maker {
    position: absolute;
    top: 752px;
    left: 0;
    width: 849px;
    text-align: center;
    font-size: 24px;
    font-weight: 800;
    letter-spacing: 0.08em;
  }
</style>
</head>
<body>
  <main class="label">
    <div class="band band--left"></div>
    <div class="band band--right"></div>

    <div class="brand-mark">
      <span class="brand-mark__dot"></span>
      <span class="brand-mark__name">実彩養和</span>
    </div>

    <h1 class="title">
      <span class="title__line">木苺と</span>
      <span class="title__line"><span class="title__fruit"><span class="title__art" role="img" aria-label="商品イラストが入る領域"></span>柚子</span>の</span>
      <span class="title__line">手仕事 <span class="title__latin">JAM</span></span>
    </h1>

    <p class="subtitle">こんふぃちゅーる</p>
    <p class="maker">実彩養和</p>
  </main>
</body>
</html>
```